New design for a company based in SF called Lumen Roads. People rent out our cars and we would like to create a subscription based platform to rent out our cars.
We rent out cars through ride nook and vela and would like people to be able to book or be redirected from our site.
Platform
I would like to have three interface.
Here are the things we need;
First interface
Company side where we can custom pricing of level subscription
level one classic; level two premiere; level 3 premium,
Second Interface-
User subscribing to the car
A subscription of low, medium, and premium
-each level needs to be based on how much miles they use per year.
-Insurance selected
This will be a custom delivery service on car
-Provide a drop off time
-minimum 1 hour notice
Third Interface
Peer to Peer Drop off-
Have people who want to get paid and select what car they would like to pick up and drop off
Create algorithm for each price to drop off due to time and distance from it destination
Updates
Need extra days to review
I emailed support and it took them 5 days to respond to find out that the designer who we select for our web design is the same designer for our logo. I need the 5 extra days because I need to fix the logo now. Thank you
Target Market(s)
domestic and international tourists travelling to San Francisco bay area-
Industry/Entity Type
Travel Industry
Logo Text
Either the name Lumen Roads or LR. I would like it to have a message within the Logo. https://www.brightsample.example/learn/hidden-meanings-behind-50-worlds-recognizable-logos/ Similar to Quorba,
Coding
Coded - Design and coding required
Number of Pages Required
1 page
Requirements
Must have
- page with what level subscription they need; Classic; Premiere, Premium
Nice to have
- calendar of availability

```html
<!DOCTYPE html>
<html lang="en">
<head>
<meta charset="utf-8">
<title>Lumen Roads — Car Subscriptions</title>
<link href="https://fonts.googleapis.com/css2?family=Montserrat:wght@400;500;600;700;800&display=swap" rel="stylesheet">
<style>
:root{
  --navy:#1b1d5c;
  --navy-deep:#15174a;
  --blue:#3d8fdc;
  --blue-soft:#5aa4e6;
  --ink:#22244a;
  --muted:#7a7d93;
  --line:#dfe2ea;
  --hero-bg:#eceef3;
  --pale:#f6f7fa;
  --white:#ffffff;
}
*{margin:0;padding:0;box-sizing:border-box}
html,body{width:1200px;height:3188px;overflow:hidden}
body{font-family:"Montserrat",Arial,sans-serif;color:var(--ink);background:var(--white);position:relative}
.abs{position:absolute}

/* Hero */
.hero{position:absolute;left:0;top:0;width:1200px;height:500px;background:linear-gradient(180deg,#f3f4f7 0%,var(--hero-bg) 100%)}
.brand{position:absolute;left:40px;top:30px;display:flex;align-items:center;gap:10px;font-weight:800;font-size:26px;color:var(--navy)}
.brand-dot{width:12px;height:12px;border-radius:50%;background:var(--blue)}
.nav{position:absolute;right:40px;top:34px;display:flex;align-items:center;gap:34px;font-size:13px;font-weight:500;color:var(--ink)}
.btn-login{background:var(--navy);color:var(--white);padding:8px 22px;border-radius:4px;font-weight:600}
.hero-title{position:absolute;left:40px;top:120px;font-size:58px;font-weight:800;color:var(--navy);line-height:1.05}
.hero-sub{position:absolute;left:40px;top:205px;font-size:22px;font-weight:500;color:var(--ink);line-height:1.3;width:360px}
.slider{position:absolute;left:40px;top:300px;width:300px}
.slider-value{font-size:20px;font-weight:700;color:var(--navy);margin-left:118px;margin-bottom:10px}
.slider-track{height:4px;background:#c9cfdb;border-radius:2px;position:relative}
.slider-fill{position:absolute;left:0;top:0;height:4px;width:140px;background:var(--blue);border-radius:2px}
.slider-knob{position:absolute;left:132px;top:-6px;width:16px;height:16px;border-radius:50%;background:var(--white);border:3px solid var(--blue)}
.slider-note{font-size:12px;color:var(--muted);margin-top:12px;margin-left:104px}
.bubble{position:absolute;border-radius:50%;display:flex;align-items:center;justify-content:center;text-align:center;color:var(--white);font-weight:700}
.bubble-blue{left:460px;top:120px;width:70px;height:70px;background:var(--blue);font-size:11px}
.bubble-navy{left:430px;top:165px;width:46px;height:46px;background:var(--navy);font-size:9px}
.hero-car{position:absolute;left:560px;top:80px;width:600px;height:360px;border-radius:50% 50% 18% 18%/40% 40% 20% 20%;background:radial-gradient(ellipse at 50% 45%,#ffffff 0%,#d7dae1 55%,#b4b8c2 100%)}

/* Why section */
.section-mark{display:block;margin:0 auto}
.why{position:absolute;left:0;top:520px;width:1200px;height:360px;text-align:center}
.h2{font-size:34px;font-weight:800;color:var(--navy);line-height:1.2}
.why-cards{position:absolute;left:140px;top:170px;width:920px;display:grid;grid-template-columns:repeat(4,1fr);gap:28px}
.why-card{height:170px;background:var(--navy);border-radius:6px;color:var(--white);display:flex;flex-direction:column;align-items:center;justify-content:center;gap:18px;padding:0 24px;font-size:12px;font-weight:500;line-height:1.4}
.why-card.is-active{background:var(--blue-soft)}

/* Features */
.features{position:absolute;left:0;top:900px;width:1200px;height:960px}
.features-title{position:absolute;left:0;top:50px;width:1200px;text-align:center}
.frame-line{position:absolute;border:2px solid var(--line)}
.feature-text{position:absolute;background:var(--white);padding:30px 34px;border-left:4px solid var(--navy)}
.feature-text h3{font-size:24px;font-weight:800;color:var(--navy);margin-bottom:16px}
.feature-text p{font-size:12px;line-height:1.7;color:var(--muted)}
.feature-text .note{margin-top:18px;padding-top:14px;border-top:1px solid var(--line);font-size:12px;color:var(--ink);font-weight:600}
.photo{position:absolute}
.photo-belt{left:600px;top:220px;width:500px;height:320px;background:linear-gradient(135deg,#2a2b33 0%,#55596a 50%,#a7b6d4 100%)}
.photo-driver{left:100px;top:550px;width:500px;height:310px;background:linear-gradient(135deg,#d8dce4 0%,#8a909e 55%,#3c3f4a 100%)}

/* Testimonials */
.reviews{position:absolute;left:0;top:1900px;width:1200px;height:460px;background:linear-gradient(180deg,var(--white) 0%,var(--pale) 100%);text-align:center}
.reviews .h2{margin-top:14px}
.review-quote{width:780px;margin:34px auto 0;font-size:14px;line-height:1.8;color:var(--muted)}
.review-source{margin-top:26px;font-size:26px;font-weight:700;color:var(--blue)}
.dots{display:flex;justify-content:center;gap:8px;margin-top:24px}
.dots span{width:9px;height:9px;border-radius:50%;background:#c8ccd8}
.dots span.on{background:var(--navy)}
.arrow{position:absolute;top:190px;font-size:26px;color:var(--navy)}

/* Pricing */
.pricing{position:absolute;left:0;top:2380px;width:1200px;height:640px;text-align:center}
.plans{position:absolute;left:240px;top:150px;display:flex;align-items:center}
.plan{width:240px;height:380px;background:var(--white);box-shadow:0 6px 24px rgba(27,29,92,.12);padding:30px 24px;text-align:left;position:relative;overflow:hidden}
.plan.is-featured{width:280px;height:430px;background:var(--navy);color:var(--white);z-index:2}
.plan-name{font-size:17px;font-weight:700}
.plan-tag{font-size:11px;color:var(--muted);margin-top:4px}
.plan.is-featured .plan-tag{color:#b6b9e0}
.plan-miles{font-size:36px;font-weight:800;margin-top:22px;line-height:1}
.plan-miles small{display:block;font-size:14px;font-weight:600;margin-top:4px}
.plan-list{list-style:none;margin-top:22px;font-size:12px;line-height:2}
.plan-list li::before{content:"✓";color:var(--blue);margin-right:10px;font-weight:700}
.plan-price{font-size:28px;font-weight:800;margin-top:20px}
.plan-price span{font-size:13px;font-weight:500}
.plan-btn{display:inline-block;margin-top:14px;background:var(--navy);color:var(--white);font-size:11px;font-weight:600;padding:9px 24px;border-radius:3px}
.plan.is-featured .plan-btn{background:var(--white);color:var(--navy)}
.plan-premium .plan-name,.plan-premium .plan-miles{color:var(--blue)}
.ribbon{position:absolute;right:-42px;top:22px;width:150px;height:22px;background:var(--blue);transform:rotate(45deg)}

/* Footer */
.footer{position:absolute;left:0;top:3020px;width:1200px;height:168px;background:var(--navy-deep);color:var(--white)}
.footer .brand{left:60px;top:60px;color:var(--white)}
.footer-cols{position:absolute;left:520px;top:30px;display:grid;grid-template-columns:repeat(4,150px);gap:10px}
.footer-cols h4{font-size:13px;font-weight:700;margin-bottom:8px}
.footer-cols a{display:block;font-size:11px;color:#b7bad8;text-decoration:none;line-height:1.7}
</style>
</head>
<body>

<header class="hero">
  <div class="brand"><span class="brand-dot"></span>Lumen Roads.</div>
  <nav class="nav">
    <span>Homepage</span><span>Why Lumen Roads</span><span>Testimonials</span><span>Pricing Plan</span>
    <span class="btn-login">Login</span>
  </nav>
  <h1 class="hero-title">Be car<br>confident.</h1>
  <p class="hero-sub" style="top:262px">Drive car with confidence without any headache</p>
  <div class="slider" style="top:352px">
    <div class="slider-value">$520</div>
    <div class="slider-track"><div class="slider-fill"></div><div class="slider-knob"></div></div>
    <div class="slider-note">1000 Miles</div>
  </div>
  <div class="bubble bubble-blue">Confident<br>drive</div>
  <div class="bubble bubble-navy">Safe<br>ride</div>
  <div class="hero-car" role="img" aria-label="Silver sports coupe photographed at a three-quarter angle"></div>
</header>

<section class="why">
  <svg class="section-mark" width="40" height="22" viewBox="0 0 40 22"><path d="M4 20 A16 16 0 0 1 36 20" fill="none" stroke="var(--navy)" stroke-width="3"/><path d="M20 20 L28 9" stroke="var(--blue)" stroke-width="3" stroke-linecap="round"/></svg>
  <h2 class="h2" style="margin-top:10px">Why get a<br>Lumen Roads.</h2>
  <div class="why-cards">
    <div class="why-card">
      <svg width="36" height="40" viewBox="0 0 36 40"><rect x="4" y="2" width="24" height="32" rx="3" fill="none" stroke="#fff" stroke-width="2.5"/><path d="M10 12h12M10 18h12M10 24h8" stroke="#fff" stroke-width="2.5"/></svg>
      No other payments hidden
    </div>
    <div class="why-card is-active">
      <svg width="40" height="36" viewBox="0 0 40 36"><rect x="2" y="8" width="34" height="22" rx="3" fill="none" stroke="#fff" stroke-width="2.5"/><circle cx="19" cy="19" r="5" fill="none" stroke="#fff" stroke-width="2.5"/></svg>
      Save your Money and Time
    </div>
    <div class="why-card">
      <svg width="40" height="36" viewBox="0 0 40 36"><circle cx="12" cy="14" r="8" fill="none" stroke="#fff" stroke-width="2.5"/><path d="M19 17 L36 17 M30 17 L30 24 M35 17 L35 22" stroke="#fff" stroke-width="2.5"/></svg>
      Easy to get Subscription within minutes
    </div>
    <div class="why-card">
      <svg width="36" height="40" viewBox="0 0 36 40"><rect x="4" y="2" width="24" height="32" rx="3" fill="none" stroke="#fff" stroke-width="2.5"/><path d="M10 12h12M10 18h12M10 24h8" stroke="#fff" stroke-width="2.5"/></svg>
      No other payments hidden
    </div>
  </div>
</section>

<section class="features">
  <div class="features-title">
    <svg class="section-mark" width="40" height="22" viewBox="0 0 40 22"><path d="M4 20 A16 16 0 0 1 36 20" fill="none" stroke="var(--navy)" stroke-width="3"/><path d="M20 20 L28 9" stroke="var(--blue)" stroke-width="3" stroke-linecap="round"/></svg>
    <h2 class="h2" style="margin-top:10px">Save, time,money<br>and much more.</h2>
  </div>
  <div class="frame-line" style="left:660px;top:190px;width:470px;height:260px"></div>
  <div class="photo photo-belt" role="img" aria-label="Close-up of a passenger fastening a seat belt"></div>
  <div class="feature-text" style="left:100px;top:270px;width:470px">
    <h3>Journeys from 1 hour.</h3>
    <p>Book a car for a short trip across the city or a full day on the coast. Pick your hour, set a drop off time and we bring the car right to your door with a full tank and clean seats ready to go.</p>
    <p class="note">More than 1 million people already using Lumen Roads for their trips.</p>
  </div>
  <div class="frame-line" style="left:70px;top:580px;width:470px;height:300px"></div>
  <div class="photo photo-driver" role="img" aria-label="Smiling driver seated behind the wheel of a car"></div>
  <div class="feature-text" style="left:640px;top:640px;width:440px;border-left:none;border-right:4px solid var(--navy)">
    <h3>Only $1 in 1 mile.</h3>
    <p>Pay only for the miles you drive each year. Every plan has insurance, roadside help and easy changes, so you know the cost before you start and never meet a surprise fee at the end of the road.</p>
    <p class="note">In this industry for a 5+ years and 98% of our clients are happy.</p>
  </div>
</section>

<section class="reviews">
  <svg class="section-mark" style="margin-top:20px" width="40" height="22" viewBox="0 0 40 22"><path d="M4 20 A16 16 0 0 1 36 20" fill="none" stroke="var(--navy)" stroke-width="3"/><path d="M20 20 L28 9" stroke="var(--blue)" stroke-width="3" stroke-linecap="round"/></svg>
  <h2 class="h2">What people are<br>saying.</h2>
  <span class="arrow" style="left:120px">‹</span>
  <span class="arrow" style="right:120px">›</span>
  <p class="review-quote">The car arrived on time at our hotel and the whole booking took a few minutes. We drove the coast for three days, paid only for our miles and dropped the car off without any stress. We will use it again on our next trip to the bay.</p>
  <div class="review-source">Revuo</div>
  <div class="dots"><span></span><span></span><span class="on"></span><span></span></div>
</section>

<section class="pricing">
  <svg class="section-mark" style="margin-top:10px" width="40" height="22" viewBox="0 0 40 22"><path d="M4 20 A16 16 0 0 1 36 20" fill="none" stroke="var(--navy)" stroke-width="3"/><path d="M20 20 L28 9" stroke="var(--blue)" stroke-width="3" stroke-linecap="round"/></svg>
  <h2 class="h2" style="margin-top:10px">Choose your<br>plan.</h2>
  <div class="plans">
    <div class="plan">
      <div class="plan-name">Low Package</div>
      <div class="plan-tag">Get started · Pay once</div>
      <div class="plan-miles">0-1000<small>Miles</small></div>
      <ul class="plan-list"><li>Insurances provided</li><li>Minimum 1 hour</li><li>Drop off details</li></ul>
      <div class="plan-price">$219<span>/year</span></div>
      <span class="plan-btn">View Package</span>
    </div>
    <div class="plan is-featured">
      <div class="plan-name">Medium Package</div>
      <div class="plan-tag">Get started · Pay once</div>
      <div class="plan-miles">1000-5000<small>Miles</small></div>
      <ul class="plan-list"><li>Insurances provided</li><li>Minimum 1 hour</li><li>Drop off details</li></ul>
      <div class="plan-price">$720<span>/year</span></div>
      <span class="plan-btn">View Package</span>
    </div>
    <div class="plan plan-premium">
      <div class="ribbon"></div>
      <div class="plan-name">Premium Package</div>
      <div class="plan-tag">Get started · Pay once</div>
      <div class="plan-miles">5000+<small>Miles</small></div>
      <ul class="plan-list"><li>Insurances provided</li><li>Minimum 1 hour</li><li>Drop off details</li></ul>
      <div class="plan-price" style="color:var(--blue)">$1090<span>/year</span></div>
      <span class="plan-btn" style="background:var(--blue)">View Package</span>
    </div>
  </div>
</section>

<footer class="footer">
  <div class="brand"><span class="brand-dot"></span>Lumen Roads.</div>
  <div class="footer-cols">
    <div><h4>Navigation</h4><a>How it Works</a><a>Pricing Page</a><a>Try Our Data</a><a>Sign up</a><a>Login</a></div>
    <div><h4>Policy</h4><a>Conditions &amp; Terms</a><a>About us</a><a>Privacy Policy</a><a>Write us</a><a>Book Security</a></div>
    <div><h4>Contacts</h4><a>Your Street Address</a><a>Phone Numbers</a><a>Email Address</a><a>Working Hours</a><a>Products</a></div>
    <div><h4>Social</h4><a>Friendnet</a><a>Pixgram</a><a>Chirper</a></div>
  </div>
</footer>

</body>
</html>
```